Cookie Box Packaging

We are looking for a Box for our Shortbread Cookies. They are traditional shortbread middle to high end of the market. Made with butter. We already have a successful product and would like to use the brand but not necessarily the style.

We like our design to be an mix of vintage and modern - we are open to all colours. The competition on the supermarket shelf is stiff and we need to stand out in grocery not in the gourmet food market. Our thinking is simple rather than the craziness and chaos that comes with a supermarket shelf.
Attached are some Box Ideas, created in-house, along with a black shortbread box idea , which we loved but didn't really fit into the grocery section of the supermarket. Make us stand out in the grocery shelf! I have also uploaded a logo. Our brand is not necessary but, is there if you wanted to use it. I have also uploaded our other product/packet design so you can see the brand of our other cookie which is positioned in bakery /deli not grocery.

I look forward to seeing the results

```html
<!DOCTYPE html>
<html lang="en">
<head>
<meta charset="utf-8">
<title>Shortbread Cookies – Box Panels</title>
<link rel="stylesheet" href="https://fonts.googleapis.com/css2?family=Montserrat:wght@500;700&family=Yellowtail&display=swap">
<style>
  :root {
    --page: #f4f4f2;
    --mint: #8ed4c3;
    --mint-light: #ace5d9;
    --lid-mint: #82c4b4;
    --lid-mint-light: #9fd3c7;
    --white: #ffffff;
    --caramel: #a8742a;
    --navy: #1d2c45;
    --brand-pink: #e58fbf;
    --cookie-light: #f3dfa6;
    --cookie-deep: #d9b774;
  }
  html, body {
    margin: 0;
    width: 1200px;
    height: 1200px;
    overflow: hidden;
    background: var(--page);
  }
  .panel {
    position: absolute;
    left: 50px;
    width: 1100px;
    overflow: hidden;
  }
  .box-lid {
    top: 280px;
    height: 250px;
    background: var(--lid-mint);
  }
  .box-front {
    top: 540px;
    height: 400px;
    background: var(--mint);
    box-shadow: 0 18px 40px rgba(0,0,0,0.12);
  }
  .hero-circle {
    position: absolute;
    border-radius: 50%;
  }
  .box-lid .hero-circle {
    left: 110px;
    top: -130px;
    width: 480px;
    height: 480px;
    background: var(--lid-mint-light);
  }
  .box-front .hero-circle {
    left: 40px;
    top: -80px;
    width: 560px;
    height: 560px;
    background: var(--mint-light);
  }
  .brand {
    position: absolute;
    display: flex;
    align-items: center;
    gap: 6px;
    font-family: "Montserrat", sans-serif;
    font-weight: 700;
    color: var(--brand-pink);
    white-space: nowrap;
  }
  .brand-dot {
    border-radius: 50%;
    background: var(--brand-pink);
  }
  .box-lid .brand { left: 170px; top: 18px; font-size: 12px; }
  .box-lid .brand-dot { width: 8px; height: 8px; }
  .box-front .brand { left: 150px; top: 34px; font-size: 16px; }
  .box-front .brand-dot { width: 10px; height: 10px; }

  .title-script,
  .title-sub,
  .claim-band {
    position: absolute;
    margin: 0;
    white-space: nowrap;
    transform: rotate(-6deg);
    transform-origin: left bottom;
  }
  .title-script {
    font-family: "Yellowtail", cursive;
    font-weight: 400;
    line-height: 1;
    color: var(--white);
  }
  .title-sub {
    font-family: "Montserrat", sans-serif;
    font-weight: 700;
    line-height: 1;
    color: var(--caramel);
  }
  .claim-band {
    background: var(--caramel);
    font-family: "Montserrat", sans-serif;
    font-weight: 500;
    line-height: 1.1;
    color: var(--white);
  }
  .box-lid .title-script { left: 120px; top: 34px; font-size: 80px; }
  .box-lid .title-sub { left: 175px; top: 128px; font-size: 34px; letter-spacing: 8px; }
  .box-lid .claim-band { left: 150px; top: 178px; font-size: 24px; padding: 2px 10px 4px; }

  .box-front .title-script { left: 95px; top: 80px; font-size: 118px; }
  .box-front .title-sub { left: 170px; top: 214px; font-size: 52px; letter-spacing: 12px; }
  .box-front .claim-band { left: 120px; top: 290px; font-size: 36px; padding: 4px 16px 6px; }

  .product-photo {
    position: absolute;
    background: radial-gradient(ellipse at 45% 40%, var(--cookie-light), var(--cookie-deep));
  }
  .box-lid .product-photo {
    left: 720px;
    top: 40px;
    width: 240px;
    height: 130px;
    border-radius: 46% / 40%;
  }
  .box-front .product-photo {
    left: 760px;
    top: 60px;
    width: 260px;
    height: 290px;
    border-radius: 48% 48% 40% 40% / 30% 30% 26% 26%;
  }
  .origin-badge {
    position: absolute;
  }
  .box-lid .origin-badge { left: 990px; top: 16px; width: 80px; height: 80px; }
  .box-front .origin-badge { left: 1000px; top: 30px; width: 90px; height: 90px; }
</style>
</head>
<body>
  <section class="panel box-lid">
    <div class="hero-circle"></div>
    <div class="brand"><span class="brand-dot"></span>Lulu Cookies</div>
    <h2 class="title-script">Shortbread</h2>
    <p class="title-sub">Cookies</p>
    <div class="claim-band">Made with Butter.</div>
    <div class="product-photo" role="img" aria-label="Photo of stacked shortbread cookies with a curl of butter"></div>
    <svg class="origin-badge" viewBox="0 0 100 100" aria-hidden="true">
      <circle cx="50" cy="50" r="46" fill="none" stroke="var(--navy)" stroke-width="3"/>
      <rect x="6" y="40" width="88" height="20" rx="10" fill="var(--navy)"/>
    </svg>
  </section>

  <section class="panel box-front">
    <div class="hero-circle"></div>
    <div class="brand"><span class="brand-dot"></span>Lulu Cookies</div>
    <h1 class="title-script">Shortbread</h1>
    <p class="title-sub">Cookies</p>
    <div class="claim-band">Made with Butter.</div>
    <div class="product-photo" role="img" aria-label="Photo of a stack of three shortbread cookies with a curl of butter"></div>
    <svg class="origin-badge" viewBox="0 0 100 100" aria-hidden="true">
      <circle cx="50" cy="50" r="46" fill="none" stroke="var(--navy)" stroke-width="3"/>
      <rect x="6" y="40" width="88" height="20" rx="10" fill="var(--navy)"/>
    </svg>
  </section>
</body>
</html>
```